Corporate Hollowmere business cards to be handed to investor, bankers etc. Needs to have a young feel

I need business cards designed for a technology company that provides vanto-like rapid response on the security industry. I would like it simple but very cool and tasteful. See attached documents for artwork and colours to be used. Cut sheet describes business model. Card stock should be thicker than normal. I would like the one side to be just the art and the other to have the contact info with maybe the pin somewhere.

Target Market(s)

Investors

Industry/Entity Type

Business

Contact Information for Business Card

Would like the logo attached on one side with name address and other info on the other side.

Font styles to use
Other font styles liked:
• See existing logo

Colors
6b449b
886aae
e4daeb
ffffff

Requirements
Must have
• Name: Gregory Thalassides
• Address: 47 Orchard Lane, Toronto, On, L6R2C8
• Tel: 647-5550192
• Email: greg@hollowmere.io
Nice to have
• See logo colours

```html
<!DOCTYPE html>
<html lang="en">
<head>
<meta charset="utf-8">
<title>Hollowmere Business Cards</title>
<link href="https://fonts.googleapis.com/css2?family=Source+Sans+3:wght@300;400&display=swap" rel="stylesheet">
<style>
  :root {
    --backdrop: #2e2925;
    --card: #0c0b0c;
    --purple: #886aae;
    --purple-deep: #6b449b;
    --lavender: #e4daeb;
    --white: #ffffff;
  }
  html, body {
    margin: 0;
    width: 1200px;
    height: 900px;
    overflow: hidden;
    background: var(--backdrop);
    font-family: "Source Sans 3", sans-serif;
  }
  .sheet {
    width: 1200px;
    height: 900px;
    display: flex;
    align-items: center;
    justify-content: center;
    gap: 60px;
  }
  .card {
    width: 525px;
    height: 300px;
    background: var(--card);
    border-radius: 3px;
    box-shadow: 0 10px 30px rgba(0,0,0,.45);
    display: flex;
    flex-direction: column;
    align-items: center;
    justify-content: center;
    color: var(--white);
    box-sizing: border-box;
  }
  .wordmark {
    display: flex;
    align-items: center;
    gap: 12px;
    font-weight: 300;
    font-size: 54px;
    letter-spacing: .5px;
    line-height: 1;
    color: var(--white);
  }
  .wordmark-dot {
    width: 26px;
    height: 26px;
    border-radius: 50%;
    background: var(--purple);
    margin-top: 8px;
  }
  .card-back .wordmark-dot { background: var(--lavender); }
  .card-back .wordmark { color: var(--lavender); }
  .holder-name {
    margin-top: 16px;
    color: var(--purple);
    font-size: 22px;
    font-weight: 400;
  }
  .contact {
    margin-top: 8px;
    font-size: 15px;
    line-height: 1.55;
    text-align: center;
  }
  .contact-label { color: var(--purple); }
  .address {
    margin-top: 12px;
    font-size: 15px;
  }
</style>
</head>
<body>
  <main class="sheet">
    <section class="card card-front">
      <div class="wordmark"><span class="wordmark-dot"></span>hollowmere</div>
      <div class="holder-name">Gregory Thalassides</div>
      <div class="contact">
        <div><span class="contact-label">P:</span> 647-5550192</div>
        <div><span class="contact-label">E:</span> greg@hollowmere.io</div>
      </div>
      <div class="address">47 Orchard Lane, Toronto, On, L6R2C8</div>
    </section>
    <section class="card card-back">
      <div class="wordmark"><span class="wordmark-dot"></span>hollowmere</div>
    </section>
  </main>
</body>
</html>
```